Copper Tide Parade

The best describe this CD is to compare it to a flower shop as a customer selects his favorite flower based on it's shape, color and aroma, the listener to this CD can select his favorite track/s. The CD contains various geners, colors and tastes. So the design must be colorful and present a bouquet either having musical notes in different beats or combination of musical notes and flowers, preferably rapped by the score lines (the five lines) and also the Sol Key somewhere in the design.

Shop

```html
<!DOCTYPE html>
<html lang="en">
<head>
<meta charset="utf-8">
<title>Copper Tide Parade</title>
<link rel="stylesheet" href="https://fonts.googleapis.com/css2?family=Parisienne&display=swap">
<style>
  :root {
    --page: #ffffff;
    --ink-title: #a8457c;
    --disc-rim: #d9d9d9;
    --hub: #e6e6e6;
    --hub-edge: #c9c9c9;
    --rule: #e3e3e3;
    --petal-red: #d8304a;
    --petal-orange: #ef6a2a;
    --petal-magenta: #b03a8e;
    --petal-blue: #1f5fb5;
    --petal-green: #7cc142;
    --mist: #f4f1f5;
  }
  html, body {
    margin: 0;
    padding: 0;
    overflow: hidden;
    background: var(--page);
  }
  .canvas {
    position: relative;
    width: 1200px;
    height: 849px;
    background: var(--page);
    overflow: hidden;
    font-family: "Parisienne", cursive;
  }
  .disc-label {
    position: absolute;
    left: 243px;
    top: 196px;
    width: 350px;
    height: 350px;
  }
  .disc-title {
    font-family: "Parisienne", cursive;
    fill: var(--ink-title);
    font-size: 30px;
  }
  .cover {
    position: absolute;
    left: 628px;
    top: 182px;
    width: 365px;
    height: 365px;
    background: var(--mist);
    overflow: hidden;
  }
  .cover-art {
    position: absolute;
    inset: 0;
    background:
      radial-gradient(circle at 30% 0%, var(--petal-red) 0%, rgba(216,48,74,0) 38%),
      radial-gradient(circle at 62% 0%, var(--petal-magenta) 0%, rgba(176,58,142,0) 35%),
      radial-gradient(circle at 5% 22%, var(--petal-orange) 0%, rgba(239,106,42,0) 30%),
      radial-gradient(circle at 0% 42%, var(--petal-blue) 0%, rgba(31,95,181,0) 26%),
      radial-gradient(circle at 0% 68%, var(--petal-green) 0%, rgba(124,193,66,0) 30%),
      var(--mist);
  }
  .cover-title {
    position: absolute;
    right: 14px;
    bottom: 14px;
    margin: 0;
    font-size: 30px;
    font-weight: 400;
    color: var(--ink-title);
    line-height: 1;
  }
  .album-title {
    position: absolute;
    left: 0;
    right: 0;
    top: 628px;
    margin: 0;
    text-align: center;
    font-size: 52px;
    font-weight: 400;
    color: var(--ink-title);
    line-height: 1;
    padding-right: 4px;
  }
  .title-rule {
    position: absolute;
    left: 115px;
    top: 705px;
    width: 977px;
    height: 2px;
    background: linear-gradient(90deg, rgba(227,227,227,0), var(--rule) 20%, var(--rule) 80%, rgba(227,227,227,0));
  }
</style>
</head>
<body>
<main class="canvas">
  <svg class="disc-label" viewBox="0 0 350 350" xmlns="http://www.w3.org/2000/svg">
    <defs>
      <radialGradient id="petal-red" cx="0.45" cy="0.05" r="0.4">
        <stop offset="0" stop-color="#d8304a"/>
        <stop offset="1" stop-color="#d8304a" stop-opacity="0"/>
      </radialGradient>
      <radialGradient id="petal-magenta" cx="0.72" cy="0.08" r="0.32">
        <stop offset="0" stop-color="#b03a8e"/>
        <stop offset="1" stop-color="#b03a8e" stop-opacity="0"/>
      </radialGradient>
      <radialGradient id="petal-orange" cx="0.22" cy="0.22" r="0.3">
        <stop offset="0" stop-color="#ef6a2a"/>
        <stop offset="1" stop-color="#ef6a2a" stop-opacity="0"/>
      </radialGradient>
      <radialGradient id="petal-blue" cx="0.05" cy="0.42" r="0.25">
        <stop offset="0" stop-color="#1f5fb5"/>
        <stop offset="1" stop-color="#1f5fb5" stop-opacity="0"/>
      </radialGradient>
      <radialGradient id="petal-green" cx="0.06" cy="0.62" r="0.28">
        <stop offset="0" stop-color="#7cc142"/>
        <stop offset="1" stop-color="#7cc142" stop-opacity="0"/>
      </radialGradient>
      <clipPath id="disc-shape">
        <circle cx="175" cy="175" r="172"/>
      </clipPath>
    </defs>
    <circle cx="175" cy="175" r="174" fill="#ffffff" stroke="var(--disc-rim)" stroke-width="2"/>
    <g clip-path="url(#disc-shape)" role="img" aria-label="Bouquet of translucent flowers in red, orange, magenta, blue and green with musical notes and staff lines">
      <rect width="350" height="350" fill="url(#petal-red)"/>
      <rect width="350" height="350" fill="url(#petal-magenta)"/>
      <rect width="350" height="350" fill="url(#petal-orange)"/>
      <rect width="350" height="350" fill="url(#petal-blue)"/>
      <rect width="350" height="350" fill="url(#petal-green)"/>
    </g>
    <circle cx="175" cy="175" r="52" fill="var(--hub)" stroke="var(--hub-edge)" stroke-width="1"/>
    <circle cx="175" cy="175" r="20" fill="#ffffff" stroke="var(--hub-edge)" stroke-width="1"/>
    <text class="disc-title" x="84" y="290">Copper Tide Parade</text>
  </svg>

  <section class="cover">
    <div class="cover-art" role="img" aria-label="Bouquet of translucent flowers in red, orange, magenta, blue and green with musical notes, staff lines and a treble clef"></div>
    <p class="cover-title">Copper Tide Parade</p>
  </section>

  <h1 class="album-title">Copper Tide Parade</h1>
  <div class="title-rule"></div>
</main>
</body>
</html>
```